Speisekarte für eine Strand-Pizzeria in Kroatien gesucht
Zielgruppe
Eine Pizzeria in einer sehr kleinen Siedlung am Meer in Kroatien, die mehr als nur Pizza anbietet. Zielgruppe sind Touristen und Ferienwohnungs-Besitzer. Die Pizzeria bietet viele verschiedene lokale und internationale Gerichte.
Aufgabenstellung
Bedient wird hauptsächlich draußen auf der Terrasse, so dass die Karten in sehr heller Umgebung im Sommer benutzt werden. Die Karte soll nicht kleiner sein als A5, aber auch nicht größer als A4.
Der Print wird später entweder laminiert oder in einer anderen langliebegen Form sein, damit die Karten mehr als 2 Saisons aushalten.
Die meisten Gerichte sollen in einer sehr schönen Form durch ein Foto dargestellt werden und intelligent angeordnet werden. Einladende Fotos brauchen wir natürlich auch (z.B. Bildarko o.ä). Bei Pizza könnte man eine Ausnahme machen und nicht jede Pizza darstellen, sondern vielleicht eine oder 2 Arten etwas größer darstellen. Eine Karte die wir sehr schön finden sind die von Teig-Kiste, vielleicht kann man sich hier anlehnen.
Die erste Seite bei zugeklappter Karte ist am wichtigsten und soll zum Essen einladen.
Das Logo ist fix (2 Palmen), aber der Schriftzug des Lokals (MELUVERA) steht noch nicht. Hier könnten wir auch eine eigene Schrift gebrauchen, die wiedererkennbar ist, da es 2 Locations gibt.
Die Karte muss in 5 Sprachen verständlich sein (siehe Fotos).
UPDATE: Sollten SIE als Designer nicht alle 5 Sprachen kennen, übernehmen Sie den Text der alten Karte (trotz Fehler). Diese Fehler können wir dann, nach Auswahl des finalen Designs verbessern.
Die aktuelle und katastrophale Karte ist angehängt (bitte beachten, dass hier sehr viele Schreibfehler sind).
UPDATE: Alle Gerichte die auf der alten Karte im Anhang angezeigt werden, sollen in Zukunft auch serviert werden.

```html
<!DOCTYPE html>
<html lang="hr">
<head>
<meta charset="utf-8">
<title>Meluvera Pizzeria – Jelovnik</title>
<link href="https://fonts.googleapis.com/css2?family=Cinzel:wght@600&family=Pinyon+Script&family=Josefin+Sans:wght@400&display=swap" rel="stylesheet">
<style>
  :root{
    --backdrop:#cdab8c;
    --cover-light:#7c420f;
    --cover-dark:#5f310a;
    --cream:#f4ece0;
    --sand:#e8d3b6;
    --rule:#eadccb;
  }
  html,body{margin:0;padding:0;width:1200px;height:900px;overflow:hidden;background:var(--backdrop);}
  .menu{
    position:absolute;left:302px;top:20px;width:596px;height:860px;
    display:flex;box-shadow:0 6px 18px rgba(60,30,5,.25);
  }
  .cover{
    position:relative;width:470px;height:100%;
    background:linear-gradient(90deg,var(--cover-light) 0%,var(--cover-light) 45%,var(--cover-dark) 100%);
  }
  .brand-disc{
    position:absolute;left:130px;top:90px;width:244px;height:244px;border-radius:50%;
    background:var(--cream);display:flex;align-items:center;justify-content:center;
  }
  .brand-disc span{
    font-family:'Cinzel',serif;font-weight:600;font-size:30px;color:var(--cover-light);letter-spacing:1px;
  }
  .title{
    position:absolute;left:0;right:0;top:340px;margin:0;text-align:center;
    font-family:'Cinzel',serif;font-weight:600;font-size:46px;letter-spacing:2px;color:var(--sand);
  }
  .subtitle{
    position:absolute;left:0;right:0;top:392px;margin:0;text-align:center;
    font-family:'Pinyon Script',cursive;font-size:42px;color:var(--sand);font-weight:400;
  }
  .languages{
    position:absolute;left:115px;top:748px;width:250px;height:30px;
  }
  .rule{
    position:absolute;left:88px;width:318px;top:792px;height:1px;background:var(--rule);
  }
  .imprint{
    position:absolute;left:0;right:0;top:803px;margin:0;text-align:center;
    font-family:'Josefin Sans',sans-serif;font-size:9.5px;line-height:12px;color:var(--sand);
  }
  .dish-strip{
    width:126px;height:100%;display:flex;flex-direction:column;gap:3px;background:#f1ebe3;
  }
  .dish-photo{flex:1;}
  .dish-pasta-mushroom{background:linear-gradient(160deg,#6d6258,#a8876a 45%,#6b5e52);}
  .dish-pizza{background:radial-gradient(circle at 45% 50%,#e0b861 0 35%,#c45a2e 36% 42%,#6a4a34 60%);}
  .dish-meatballs{background:linear-gradient(180deg,#8a3a22,#b64a2a 55%,#f1e6c8 80%,#ddd 100%);}
  .dish-spaghetti{background:linear-gradient(170deg,#8c8474,#e9dfd2 40%,#c9472d 60%,#f2eae4 85%);}
  .dish-salad{background:linear-gradient(150deg,#8a8c86,#7ea24a 50%,#c6c7c1 80%);}
</style>
</head>
<body>
  <main class="menu">
    <section class="cover">
      <div class="brand-disc"><span>MELUVERA</span></div>
      <h1 class="title">MELUVERA</h1>
      <h2 class="subtitle">Pizzeria</h2>

      <svg class="languages" viewBox="0 0 250 30" role="img" aria-label="Jezici: hrvatski, talijanski, njemački, engleski, slovenski">
        <defs>
          <clipPath id="flag-hr"><circle cx="15" cy="15" r="13"/></clipPath>
          <clipPath id="flag-it"><circle cx="69" cy="15" r="13"/></clipPath>
          <clipPath id="flag-de"><circle cx="123" cy="15" r="13"/></clipPath>
          <clipPath id="flag-gb"><circle cx="176" cy="15" r="13"/></clipPath>
          <clipPath id="flag-si"><circle cx="236" cy="15" r="13"/></clipPath>
        </defs>
        <g clip-path="url(#flag-hr)">
          <rect x="0" y="0" width="30" height="10" fill="#d52b1e"/>
          <rect x="0" y="10" width="30" height="10" fill="#fff"/>
          <rect x="0" y="20" width="30" height="10" fill="#1b3f95"/>
        </g>
        <g clip-path="url(#flag-it)">
          <rect x="54" y="0" width="10" height="30" fill="#009246"/>
          <rect x="64" y="0" width="10" height="30" fill="#fff"/>
          <rect x="74" y="0" width="10" height="30" fill="#ce2b37"/>
        </g>
        <g clip-path="url(#flag-de)">
          <rect x="108" y="0" width="30" height="10" fill="#111"/>
          <rect x="108" y="10" width="30" height="10" fill="#dd0000"/>
          <rect x="108" y="20" width="30" height="10" fill="#ffce00"/>
        </g>
        <g clip-path="url(#flag-gb)">
          <rect x="161" y="0" width="30" height="30" fill="#012169"/>
          <path d="M161 0L191 30M191 0L161 30" stroke="#fff" stroke-width="5"/>
          <path d="M161 0L191 30M191 0L161 30" stroke="#c8102e" stroke-width="1.6"/>
          <path d="M176 0V30M161 15H191" stroke="#fff" stroke-width="7"/>
          <path d="M176 0V30M161 15H191" stroke="#c8102e" stroke-width="4"/>
        </g>
        <g clip-path="url(#flag-si)">
          <rect x="221" y="0" width="30" height="10" fill="#fff"/>
          <rect x="221" y="10" width="30" height="10" fill="#0a3d9c"/>
          <rect x="221" y="20" width="30" height="10" fill="#ed1c24"/>
        </g>
        <g fill="none" stroke="#fff" stroke-width="1.2">
          <circle cx="15" cy="15" r="13"/><circle cx="69" cy="15" r="13"/><circle cx="123" cy="15" r="13"/><circle cx="176" cy="15" r="13"/><circle cx="236" cy="15" r="13"/>
        </g>
      </svg>

      <div class="rule"></div>
      <p class="imprint">"PIZZERIA MELUVERA, LUČICA SVETI ROK 4B,<br>SELVINA, Vl. Dorin Valček, OIB: 51837264091"</p>
    </section>

    <aside class="dish-strip">
      <div class="dish-photo dish-pasta-mushroom" role="img" aria-label="Fotografija: špageti s gljivama na tanjuru"></div>
      <div class="dish-photo dish-pizza" role="img" aria-label="Fotografija: pizza s rajčicom i sirom"></div>
      <div class="dish-photo dish-meatballs" role="img" aria-label="Fotografija: mesne okruglice u umaku od rajčice na špagetima"></div>
      <div class="dish-photo dish-spaghetti" role="img" aria-label="Fotografija: špageti s cherry rajčicama i bosiljkom"></div>
      <div class="dish-photo dish-salad" role="img" aria-label="Fotografija: salata od tjestenine s povrćem"></div>
    </aside>
  </main>
</body>
</html>
```